Social Media Post Quote #5 - Native American Organization

- GATHER - must be included
- Protect your community. Protect Your Elders. Stay Vaccinated. must be included
- Attached, company Logo, campaign logos and sample flu social media image. - our audience likes BRIGHT colors.
- Must include image from the United States, representing Land/Nature from one of the following regions, Plains and Woodlands, or Southwest, or Mountains, or Coast.
- must include quote: Help our “early elders” achieve “older elders” status.
- One image will be provided twice - incorporating campaign logos - in some fashion
Inspiration: https://velmorhub.example/ and https://www.facebook.com/Velmorhub

```html
<!DOCTYPE html>
<html lang="en">
<head>
<meta charset="utf-8">
<title>GATHER – Help our early elders</title>
<link rel="stylesheet" href="https://fonts.googleapis.com/css2?family=Barlow:wght@400;500&family=Barlow+Condensed:wght@400;600&family=Montserrat:wght@700&display=swap">
<style>
  :root {
    --canvas: #ffffff;
    --cream: #f3e8df;
    --white: #ffffff;
    --quote-fill: rgba(214, 38, 104, 0.82);
    --tagline: #b4504c;
    --org: #b4504c;
    --teal: #4ea6af;
    --brown: #5a321b;
    --brick: #b65656;
    --crimson: #9a1f36;
  }
  * { margin: 0; padding: 0; box-sizing: border-box; }
  html, body {
    width: 1200px; height: 372px; overflow: hidden;
    background: var(--canvas);
  }
  .post-row { position: relative; width: 1200px; height: 372px; }
  .post {
    position: absolute; top: 0; width: 374px; height: 372px;
    background: var(--cream); overflow: hidden;
  }
  .post--flu { left: 39px; --frame: var(--teal); --word: var(--brown); }
  .post--both { left: 414px; --frame: var(--brick); --word: var(--teal); }
  .post--covid { left: 789px; --frame: var(--white); --word: var(--crimson); }

  .scene {
    position: absolute; inset: 0 0 80px 0;
    background:
      radial-gradient(ellipse 45% 30% at 30% 30%, rgba(240,60,110,0.9), transparent 70%),
      radial-gradient(ellipse 45% 30% at 72% 28%, rgba(250,110,140,0.85), transparent 70%),
      radial-gradient(ellipse 60% 18% at 50% 70%, rgba(230,90,110,0.55), transparent 70%),
      linear-gradient(180deg, #4b4a1c 0%, #2f3318 30%, #3a3a22 55%, #8a6a55 80%, var(--cream) 100%);
  }
  .headline {
    position: absolute; top: 19px; left: 0; width: 100%;
    text-align: center; color: var(--white); white-space: nowrap;
    font: 500 12.2px/1 "Barlow", sans-serif; letter-spacing: 0.1px;
  }
  .post--both .headline { font-size: 11px; }
  .quote-box {
    position: absolute; left: 57px; top: 102px; width: 259px; height: 132px;
    background: var(--quote-fill); border: 1px solid var(--white);
    display: flex; align-items: center; justify-content: center;
    padding-top: 6px;
  }
  .quote-mark {
    position: absolute; left: 50%; top: 72px; transform: translateX(-50%);
    color: var(--white); font: 700 80px/1 "Montserrat", sans-serif;
  }
  .quote-text {
    color: var(--white); text-align: center; white-space: nowrap;
    font: 400 29px/24px "Barlow Condensed", sans-serif; letter-spacing: -0.4px;
  }
  .campaign {
    position: absolute; left: 19px; top: 292px; width: 186px; height: 43px;
    border: 2.5px solid var(--frame);
    display: flex; align-items: center; justify-content: center;
    color: var(--word); font: 700 33px/1 "Montserrat", sans-serif; letter-spacing: 1px;
  }
  .org {
    position: absolute; left: 225px; top: 302px; width: 140px;
    display: flex; align-items: center; gap: 8px;
  }
  .org-mark { width: 22px; height: 22px; background: var(--org); flex: none; }
  .org-name {
    color: var(--org); font: 600 11px/1.05 "Barlow Condensed", sans-serif;
    text-transform: uppercase; white-space: nowrap;
  }
  .tagline {
    position: absolute; left: 18px; top: 344px; white-space: nowrap;
    color: var(--tagline); font: 400 10.3px/1 "Barlow", sans-serif; letter-spacing: 0.1px;
  }
</style>
</head>
<body>
<main class="post-row">
  <article class="post post--flu">
    <div class="scene" role="img" aria-label="Two roseate spoonbills with pink wings spread, wading in calm water at sunset"></div>
    <p class="headline">LEARN MORE ABOUT GETTING VACCINATED AGAINST THE FLU</p>
    <blockquote class="quote-box"><p class="quote-text">Help our<br>“early elders”<br>achieve<br>“older elders” status</p></blockquote>
    <span class="quote-mark" aria-hidden="true">“</span>
    <div class="campaign">GATHER</div>
    <div class="org"><span class="org-mark"></span><span class="org-name">Velmor Hub<br>Elder Network</span></div>
    <p class="tagline">PROTECT YOUR COMMUNITY. PROTECT YOUR ELDERS. STAY VACCINATED.</p>
  </article>

  <article class="post post--both">
    <div class="scene" role="img" aria-label="Two roseate spoonbills with pink wings spread, wading in calm water at sunset"></div>
    <p class="headline">LEARN MORE ABOUT GETTING VACCINATED AGAINST COVID-19 &amp; THE FLU</p>
    <blockquote class="quote-box"><p class="quote-text">Help our<br>“early elders”<br>achieve<br>“older elders” status</p></blockquote>
    <span class="quote-mark" aria-hidden="true">“</span>
    <div class="campaign">GATHER</div>
    <div class="org"><span class="org-mark"></span><span class="org-name">Velmor Hub<br>Elder Network</span></div>
    <p class="tagline">PROTECT YOUR COMMUNITY. PROTECT YOUR ELDERS. STAY VACCINATED.</p>
  </article>

  <article class="post post--covid">
    <div class="scene" role="img" aria-label="Two roseate spoonbills with pink wings spread, wading in calm water at sunset"></div>
    <p class="headline">LEARN MORE ABOUT GETTING VACCINATED AGAINST COVID-19</p>
    <blockquote class="quote-box"><p class="quote-text">Help our<br>“early elders”<br>achieve<br>“older elders” status</p></blockquote>
    <span class="quote-mark" aria-hidden="true">“</span>
    <div class="campaign">GATHER</div>
    <div class="org"><span class="org-mark"></span><span class="org-name">Velmor Hub<br>Elder Network</span></div>
    <p class="tagline">PROTECT YOUR COMMUNITY. PROTECT YOUR ELDERS. STAY VACCINATED.</p>
  </article>
</main>
</body>
</html>
```